clean web design for a recruitment company

We need a web design for a company called 'TORAVI' recruitment. We are a new age recruitment companies that selects people by their true nature, values and what they can bring to the table as a tangible talent. We are all here possessing a certain talent, whatever that could be that the world needs. The final design should communicate professionalism and strongly embedded etiquette we believe in and a branding promise 'Seeing ones true nature'. Our companies values are integrity, giving away to the community, cherishing the sharing of our talent, time and helping one another.

Target Market(s)

Gulf Countries

Industry/Entity Type

It Company

Number of Pages Required

1 page

Font styles to use
Serif

Requirements
Must have
• Clear and readable font, user friendly structure and easy navigation menus.
Nice to have
• Extra sort of ideas on images we may use, tag lines etc. sample sites we love site:https://www.velmaroque.com/
• http://www.dorisaklund.com/
• http://www.pebblemoorhouse.com/idea-gallery/
Should not have
• all sort of colors, big combination of fonts, images with people in the office or people in suits likewise all the typical industry web sites

```html
<!DOCTYPE html>
<html lang="en">
<head>
<meta charset="utf-8">
<title>Toravi Recruitment</title>
<link rel="stylesheet" href="https://fonts.googleapis.com/css2?family=Roboto+Condensed:wght@700&family=Courier+Prime:ital,wght@0,400;0,700;1,700&family=Poppins:wght@200;300;400&display=swap">
<style>
  :root {
    --ink: #000;
    --paper: #fff;
    --panel: #555;
    --rule: #222;
    --muted: #333;
  }
  * { box-sizing: border-box; margin: 0; padding: 0; }
  html, body { width: 1200px; height: 750px; overflow: hidden; background: var(--paper); }
  .page { position: relative; width: 1200px; height: 750px; font-family: "Poppins", sans-serif; color: var(--ink); }

  .brand { position: absolute; left: 132px; top: 6px; width: 70px; text-align: center; }
  .brand-mark { display: block; width: 20px; height: 40px; margin: 0 auto 8px; background: var(--ink); }
  .brand-name { font-family: "Poppins", sans-serif; font-weight: 400; font-size: 16px; line-height: 1; letter-spacing: .5px; }
  .brand-sub { font-family: "Poppins", sans-serif; font-weight: 400; font-size: 6px; letter-spacing: 1.6px; margin-top: 3px; }

  .main-nav { position: absolute; left: 327px; top: 0; width: 651px; height: 74px; background: var(--ink); }
  .main-nav a { position: absolute; top: 27px; font-family: "Roboto Condensed", sans-serif; font-weight: 700; font-size: 15px; color: var(--paper); text-decoration: none; white-space: nowrap; }

  .login { position: absolute; left: 1038px; top: 28px; font-family: "Roboto Condensed", sans-serif; font-weight: 700; font-size: 15px; }
  .search { position: absolute; left: 1145px; top: 28px; }

  .top-rule { position: absolute; left: 0; top: 85px; width: 1200px; height: 12px; background: var(--ink); }

  .slider { position: absolute; left: 83px; top: 97px; width: 1034px; height: 332px; display: flex; }
  .slide-a { width: 535px; background: linear-gradient(180deg, #3a3d3d 0%, #8a8f8e 45%, #6c7170 75%, #4b4f4e 100%); }
  .slide-b { width: 246px; background: radial-gradient(circle at 62% 45%, #3a3a3a 0%, #0b0b0b 45%, #000 80%); }
  .slide-c { width: 253px; background: linear-gradient(180deg, #5a5a5a 0%, #c9c9c9 35%, #8c8c8c 65%, #2e2e2e 100%); }
  .arrow { position: absolute; top: 250px; }

  .tagline-band { position: absolute; left: 0; top: 429px; width: 1200px; height: 65px; background: var(--ink); color: var(--paper); text-align: center; font-family: "Poppins", sans-serif; font-weight: 200; font-size: 52px; line-height: 68px; letter-spacing: .3px; overflow: hidden; padding-left: 80px; }

  .address { position: absolute; left: 14px; top: 535px; width: 198px; height: 85px; border: 1px solid var(--ink); padding: 6px 6px; font-family: "Courier Prime", monospace; font-weight: 700; font-style: italic; font-size: 13px; line-height: 17.5px; white-space: nowrap; overflow: hidden; }

  .unique { position: absolute; left: 233px; top: 505px; width: 545px; height: 154px; background: var(--panel); color: var(--paper); padding: 17px 13px; font-family: "Courier Prime", monospace; font-size: 14.6px; line-height: 18px; white-space: nowrap; letter-spacing: .1px; }

  .footer-col { position: absolute; top: 528px; font-family: "Poppins", sans-serif; font-weight: 300; font-size: 9px; line-height: 12px; color: var(--muted); }
  .footer-col h3 { font-weight: 400; font-size: 10px; color: var(--ink); margin-bottom: 14px; }
  .footer-col li { list-style: none; }
  .col-support { left: 812px; }
  .col-links { left: 967px; }
  .col-about { left: 1098px; }
  .divider { position: absolute; top: 526px; width: 1px; height: 106px; background: var(--rule); }

  .bottom-bar { position: absolute; left: 0; top: 709px; width: 1200px; height: 41px; background: var(--ink); }
  .copyright { position: absolute; left: 0; width: 1235px; top: 13px; text-align: center; color: var(--paper); font-family: "Courier Prime", monospace; font-weight: 700; font-size: 10px; }
  .social { position: absolute; left: 927px; top: 8px; display: flex; gap: 12px; }
  .social span { display: flex; align-items: center; justify-content: center; width: 27px; height: 27px; border-radius: 4px; background: var(--paper); }
  .social span::after { content: ""; width: 11px; height: 11px; border-radius: 50%; background: var(--ink); }
</style>
</head>
<body>
<div class="page">

  <header>
    <div class="brand">
      <span class="brand-mark"></span>
      <div class="brand-name">toravi</div>
      <div class="brand-sub">RECRUITMENT</div>
    </div>

    <nav class="main-nav">
      <a style="left:58px">Home</a>
      <a style="left:121px">Team</a>
      <a style="left:178px">Methodology</a>
      <a style="left:272px">Specialist Atreas</a>
      <a style="left:389px">Clinets</a>
      <a style="left:452px">Candidates</a>
      <a style="left:537px">Toravi Group</a>
    </nav>

    <div class="login">LOGIN</div>
    <svg class="search" width="20" height="20" viewBox="0 0 20 20" aria-label="Search">
      <circle cx="8" cy="8" r="5.5" fill="none" stroke="#000" stroke-width="2.4"/>
      <line x1="12" y1="12" x2="18" y2="18" stroke="#000" stroke-width="3" stroke-linecap="round"/>
    </svg>
  </header>

  <div class="top-rule"></div>

  <section class="slider">
    <div class="slide-a" role="img" aria-label="Gallery wall of black and white portraits with a visitor walking past"></div>
    <div class="slide-b" role="img" aria-label="Dark portrait emerging from shadow"></div>
    <div class="slide-c" role="img" aria-label="Black and white interior of an arcaded hall"></div>
  </section>

  <svg class="arrow" style="left:21px" width="27" height="27" viewBox="0 0 27 27" aria-label="Previous slide">
    <circle cx="13.5" cy="13.5" r="12" fill="#fff" stroke="#000" stroke-width="2.5"/>
    <polyline points="15.5,8 10,13.5 15.5,19" fill="none" stroke="#000" stroke-width="3" stroke-linecap="round" stroke-linejoin="round"/>
  </svg>
  <svg class="arrow" style="left:1141px" width="27" height="27" viewBox="0 0 27 27" aria-label="Next slide">
    <circle cx="13.5" cy="13.5" r="12" fill="#fff" stroke="#000" stroke-width="2.5"/>
    <polyline points="11.5,8 17,13.5 11.5,19" fill="none" stroke="#000" stroke-width="3" stroke-linecap="round" stroke-linejoin="round"/>
  </svg>

  <h1 class="tagline-band">Seeing ones true nature</h1>

  <address class="address">4120 Marlow Crescent,<br>Dunmere, DC 45 Fr<br>45.contact@sample-<br>mail.org+1 800 372 914</address>

  <section class="unique">
    What makes us unique?<br>
    We do recruitment based on ones belongings and purpose in<br>
    life. Finding that purpose in life, and just aligning<br>
    ones values to correspond with the company one wishes to<br>
    apply. Our branding is guided by genuinely, trustworthy,<br>
    helping one another and making the world a better place<br>
    to be in!
  </section>

  <div class="footer-col col-support">
    <h3>Support Menu</h3>
    <ul>
      <li>Lost Password?</li>
      <li>Forgot your Username?</li>
      <li>Your Membership</li>
      <li>Your Account</li>
      <li>Support Forum</li>
      <li>Important Links</li>
    </ul>
  </div>
  <div class="divider" style="left:935px"></div>
  <div class="footer-col col-links">
    <h3>Impostant links</h3>
    <ul>
      <li>Affiliate Program</li>
      <li>Special Promotions</li>
      <li>Newsletter</li>
      <li>Contact</li>
    </ul>
  </div>
  <div class="divider" style="left:1073px"></div>
  <div class="footer-col col-about">
    <h3>About Us</h3>
    <ul>
      <li>Customer focus</li>
      <li>Performance</li>
      <li>Innovation</li>
      <li>Responsibility</li>
    </ul>
  </div>

  <footer class="bottom-bar">
    <div class="copyright">@Copyright</div>
    <div class="social" aria-label="Social links">
      <span></span><span></span><span></span><span></span><span></span><span></span><span></span>
    </div>
  </footer>

</div>
</body>
</html>
```